CREATE A BUSINESS CARD FOR A BOAT CLEANING SERVICE

WE ARE STARTING A NEW BOAT CLEANING BUSINESS. WE DIVE UNDERWATER TO CLEAN BOAT HULLS, JETTIES, UNDERWATER STRUCTURES ETC. WE ARE LOOKING FOR AN UPPERMARKET MODERN LOGO AND BUSINESS CARD AS ALOT OF OUR TARGET MARKET WILL BE HIGH END. YOU HAVE TO DESIGN A BUSINESS CARD AND LOGO SEPERATELY .
THE BUSINESS CARD DIMESNION MUST BE STANDARD SIZE.
The standard dimensions of a printed business card are 3.5 x 2 inches

Target Market(s)

UNDERWATER SERVICED

Industry/Entity Type

Business

Contact Information for Business Card

HALDEN UNDERWATER SERVICES

Font styles to use
Serif

Colors

Designer to choose colors to be used in the design.

Requirements
Must have
• HALDEN
Nice to have
• dark
Should not have
• more than 3 colors

```html
<!DOCTYPE html>
<html lang="en">
<head>
<meta charset="utf-8">
<title>Halden Underwater Services — Identity Sheet</title>
<link href="https://fonts.googleapis.com/css2?family=Hind:wght@400;500;600;700&display=swap" rel="stylesheet">
<style>
  :root{
    --brand-blue:#1a4a8f;
    --ink-grey:#5b5b5d;
    --ink-black:#111111;
    --paper:#ffffff;
    --stage:#efe9df;
    --frame:#1b1b1b;
    --font:"Hind", Arial, sans-serif;
  }
  *{margin:0;padding:0;box-sizing:border-box}
  html,body{width:960px;height:1200px;overflow:hidden;background:var(--paper);font-family:var(--font)}
  .sheet{position:relative;width:960px;height:1200px}

  .wordmark{position:absolute;text-align:center;font-weight:700;line-height:1;white-space:nowrap}
  .wordmark .name{display:block;letter-spacing:1px}
  .wordmark .tagline{display:block;letter-spacing:.5px}
  .wordmark--primary{left:104px;top:300px;width:424px;color:var(--brand-blue)}
  .wordmark--primary .name{font-size:104px}
  .wordmark--primary .tagline{font-size:30px;margin-top:6px;color:var(--ink-grey)}
  .wordmark--mono{left:585px;top:336px;width:290px;color:var(--ink-black)}
  .wordmark--mono .name{font-size:72px}
  .wordmark--mono .tagline{font-size:20px;margin-top:4px}

  .presentation{position:absolute;left:22px;top:492px;width:912px;height:658px;border:1.5px solid var(--frame);background:var(--stage)}
  .presentation .divider{position:absolute;left:458px;top:0;bottom:0;border-left:1.5px solid var(--frame)}

  .card{position:absolute;width:390px;height:222px;overflow:hidden}
  .card--front{background:var(--brand-blue);color:var(--paper)}
  .card--back{background:var(--paper)}
  .card--front .wordmark{left:0;right:0;top:78px;color:var(--paper)}
  .card--front .wordmark .name{font-size:56px}
  .card--front .wordmark .tagline{font-size:17px;margin-top:2px}

  .holder{position:absolute;width:160px;text-align:center;color:var(--brand-blue);white-space:nowrap}
  .holder .person{font-size:21px;font-weight:700;line-height:1;letter-spacing:.5px}
  .holder .role{font-size:12px;font-weight:600;color:var(--ink-grey);line-height:1.1}
  .address{position:absolute;font-size:12px;line-height:15px;color:var(--brand-blue);white-space:nowrap}
  .contact{position:absolute;list-style:none}
  .contact li{position:absolute;left:0;display:flex;align-items:center;white-space:nowrap;color:var(--brand-blue);font-size:14.5px}
  .contact li.small{font-size:12.5px}
  .contact svg{width:24px;height:24px;margin-right:14px;flex:none}

  .card--back .wordmark{color:var(--brand-blue)}
  .card--back .wordmark .name{font-size:34px}
  .card--back .wordmark .tagline{font-size:10.5px;margin-top:1px;letter-spacing:.3px;color:var(--ink-grey)}

  .card-wave{position:absolute;left:0;bottom:0;width:390px;height:52px}
  .card-rule{position:absolute;left:173px;top:38px;width:1.5px;height:146px;background:var(--ink-grey)}

  .style-label{position:absolute;width:390px;text-align:center;font-size:18px;font-weight:700;color:var(--ink-grey);line-height:23px;letter-spacing:.5px}
</style>
</head>
<body>
<main class="sheet">

  <div class="wordmark wordmark--primary"><span class="name">HALDEN</span><span class="tagline">UNDERWATER SERVICES</span></div>
  <div class="wordmark wordmark--mono"><span class="name">HALDEN</span><span class="tagline">UNDERWATER SERVICES</span></div>

  <section class="presentation">
    <div class="divider"></div>

    <!-- Style 3 -->
    <div class="card card--front" style="left:34px;top:42px">
      <div class="wordmark"><span class="name">HALDEN</span><span class="tagline">UNDERWATER SERVICES</span></div>
    </div>
    <div class="card card--back" style="left:34px;top:308px">
      <div class="holder" style="left:38px;top:38px">
        <div class="person">YOUR NAME</div><div class="role">PRESIDENT</div>
      </div>
      <p class="address" style="left:36px;top:72px">Your address Lorem ispum abc<br>Lorem ispum Lorem ispum abc</p>
      <ul class="contact" style="left:36px;top:0">
        <li style="top:109px"><svg viewBox="0 0 24 24"><circle cx="12" cy="12" r="11" fill="none" stroke="#5b5b5d" stroke-width="1"/><rect x="6" y="8" width="12" height="8" fill="#5b5b5d"/><path d="M6 8l6 5 6-5" fill="none" stroke="#fff" stroke-width="1"/></svg>hello@haldendive.com</li>
        <li style="top:139px"><svg viewBox="0 0 24 24"><circle cx="12" cy="12" r="11" fill="none" stroke="#5b5b5d" stroke-width="1"/><rect x="8.5" y="5.5" width="7" height="13" rx="1.2" fill="none" stroke="#5b5b5d" stroke-width="1.4"/><circle cx="12" cy="16.3" r=".8" fill="#5b5b5d"/></svg>+012 - 4471 - 20958</li>
        <li class="small" style="top:167px"><svg viewBox="0 0 24 24"><circle cx="12" cy="12" r="11" fill="none" stroke="#5b5b5d" stroke-width="1"/><circle cx="12" cy="12" r="6.5" fill="none" stroke="#5b5b5d" stroke-width="1.3"/><ellipse cx="12" cy="12" rx="3" ry="6.5" fill="none" stroke="#5b5b5d" stroke-width="1.1"/><path d="M5.5 12h13M6.5 9h11M6.5 15h11" stroke="#5b5b5d" stroke-width="1"/></svg>haldenunderwater.com</li>
      </ul>
      <div class="wordmark" style="left:224px;top:120px;width:134px"><span class="name">HALDEN</span><span class="tagline">UNDERWATER SERVICES</span></div>
      <svg class="card-wave" viewBox="0 0 390 52" preserveAspectRatio="none"><path d="M0 22 C90 8 140 40 230 28 C300 18 340 2 390 4 L390 52 L0 52 Z" fill="var(--ink-grey)"/></svg>
    </div>
    <p class="style-label" style="left:34px;top:568px">BUSINESS CARD<br>STYLE 3</p>

    <!-- Style 4 -->
    <div class="card card--front" style="left:492px;top:42px">
      <div class="wordmark"><span class="name">HALDEN</span><span class="tagline">UNDERWATER SERVICES</span></div>
    </div>
    <div class="card card--back" style="left:492px;top:308px">
      <div class="wordmark" style="left:24px;top:122px;width:136px"><span class="name">HALDEN</span><span class="tagline">UNDERWATER SERVICES</span></div>
      <div class="card-rule"></div>
      <div class="holder" style="left:190px;top:36px">
        <div class="person">YOUR NAME</div><div class="role">PRESIDENT</div>
      </div>
      <p class="address" style="left:190px;top:70px">Your address Lorem ispum abc<br>Lorem ispum Lorem ispum abc</p>
      <ul class="contact" style="left:189px;top:0">
        <li style="top:106px"><svg viewBox="0 0 24 24"><circle cx="12" cy="12" r="11" fill="none" stroke="#5b5b5d" stroke-width="1"/><rect x="6" y="8" width="12" height="8" fill="#5b5b5d"/><path d="M6 8l6 5 6-5" fill="none" stroke="#fff" stroke-width="1"/></svg>hello@haldendive.com</li>
        <li style="top:135px"><svg viewBox="0 0 24 24"><circle cx="12" cy="12" r="11" fill="none" stroke="#5b5b5d" stroke-width="1"/><rect x="8.5" y="5.5" width="7" height="13" rx="1.2" fill="none" stroke="#5b5b5d" stroke-width="1.4"/><circle cx="12" cy="16.3" r=".8" fill="#5b5b5d"/></svg>+012 - 4471 - 20958</li>
        <li class="small" style="top:164px"><svg viewBox="0 0 24 24"><circle cx="12" cy="12" r="11" fill="none" stroke="#5b5b5d" stroke-width="1"/><circle cx="12" cy="12" r="6.5" fill="none" stroke="#5b5b5d" stroke-width="1.3"/><ellipse cx="12" cy="12" rx="3" ry="6.5" fill="none" stroke="#5b5b5d" stroke-width="1.1"/><path d="M5.5 12h13M6.5 9h11M6.5 15h11" stroke="#5b5b5d" stroke-width="1"/></svg>haldenunderwater.com</li>
      </ul>
    </div>
    <p class="style-label" style="left:492px;top:565px">BUSINESS CARD<br>STYLE 4</p>
  </section>

</main>
</body>
</html>
```